Webdesign für Maklerbüro
Zielgruppe
Wir sind ein Maklerbüro aus Nürnberg, das sich auf den Verkauf von Eigentumswohnungen und Häuser spezialisiert hat. Mit der neuen Seite möchten wir vor allem Eigentümer ansprechen und über unsere Arbeitsweise informieren. Der Hauptzweck ist damit die Akquise von neuen Objekten, für die Vermittlung. Die Zielgruppe sind vornehmlich Immobilienbesitzer im Alter 40+ und im gehobenen Preissegment.
Aufgabenstellung
Beim Design bitte an den Vorgaben des Logo (Datei beigefügt) orientieren. Bilder und Texte können durch 'Platzhalter' ersetzt werden.
Grundsätzlich stellt es für uns kein Problem dar, sich an Template-Vorlagen zu orientieren. Wir stellen uns eine Seite mit Pfiff und Ideenreichtum – einfach weg vom Standard – vor. Wir verkaufen Immobilien, aber vom verstaubten Krawattenträger sind wir weit entfernt. Wir sind ein junges Unternehmen, das neue Marketingwege beschreitet. Unsere Webseite muss das ausdrücken. Kein Standard, und damit auch keine Standard-Webseite. Designs, die uns gut gefallen (und in die Richtung es auch gehen kann) haben wir beigefügt.

```html
<!DOCTYPE html>
<html lang="de">
<head>
<meta charset="utf-8">
<title>Wohnwerk Franken – Immobilienmakler</title>
<link href="https://fonts.googleapis.com/css2?family=Montserrat:wght@500;600;700;800&family=Nunito+Sans:ital,wght@0,400;0,600;0,700;1,400&display=swap" rel="stylesheet">
<style>
:root{
  --navy:#1b2540;
  --navy-dark:#2f3349;
  --blue:#0b8fd3;
  --grey:#eeeeee;
  --text:#3a3a3a;
  --white:#ffffff;
}
*{box-sizing:border-box;margin:0;padding:0}
html,body{width:1200px;height:3785px;overflow:hidden}
body{font-family:'Nunito Sans',sans-serif;color:var(--text);background:var(--white);position:relative}
.abs{position:absolute}
h1,h2,h3,.brand,.btn{font-family:'Montserrat',sans-serif}

/* hero */
.hero{position:absolute;left:0;top:0;width:1200px;height:570px;
  background:linear-gradient(180deg,#1d2b4d 0%,#2c3a5c 45%,#5a4c4a 80%,#6e5448 100%)}
.brand{font-weight:800;letter-spacing:.5px;display:flex;align-items:center;gap:8px}
.brand .mark{width:14px;height:14px;display:inline-block}
.brand-hero{left:126px;top:46px;color:var(--white);font-size:16px}
.brand-hero .mark{background:var(--white)}
.nav{right:96px;top:48px;display:flex;gap:25px;color:var(--white);font-size:12.5px}
.hero h1{left:126px;top:176px;color:var(--white);font-size:34px;font-weight:700;line-height:41px}
.tile{top:304px;width:137px;height:135px;border:1.5px solid var(--white);color:var(--white)}
.tile svg{position:absolute;left:10px;top:10px}
.tile span{position:absolute;right:12px;bottom:9px;text-align:right;font-family:'Montserrat',sans-serif;font-weight:700;font-size:13px;line-height:16px}

/* intro */
.intro{position:absolute;left:0;top:570px;width:1200px;height:526px;background:var(--grey)}
.intro h2{left:448px;top:82px;color:var(--blue);font-size:25px;font-weight:700}
.intro p{left:448px;width:622px;font-size:11.4px;line-height:18.6px;color:#555}
.intro .cta-q{left:449px;top:418px;font-family:'Montserrat',sans-serif;font-weight:700;font-size:12.5px;color:#222}
.btn{background:var(--navy);color:var(--white);font-weight:700;font-size:12px;display:flex;align-items:center;justify-content:center}
.intro .btn{left:726px;top:402px;width:204px;height:41px}

/* services */
.kicker{left:125px;top:1210px;font-size:12.5px;color:#222}
.services-title{left:125px;top:1232px;color:var(--blue);font-size:26px;font-weight:700}
.all-link{left:125px;top:1274px;font-size:12.5px;color:#222;text-decoration:underline;font-weight:600}
.grid{left:125px;top:1316px;width:950px;height:475px}
.cell{position:absolute;width:237.5px;height:237.5px}
.ph{position:absolute}
.cell-blue{background:var(--blue);color:var(--white);padding:40px 17px 0}
.cell-text{padding:44px 0 0 0;color:#333}
.cell-text.right{padding-left:37px}
.cell h3{font-family:'Nunito Sans',sans-serif;font-weight:600;font-size:12.5px;letter-spacing:.3px;margin-bottom:10px}
.cell p{font-size:12.3px;line-height:17.5px}
.notch{position:absolute;width:0;height:0;border-top:12px solid transparent;border-bottom:12px solid transparent}

/* testimonials */
.reviews{position:absolute;left:0;top:1901px;width:1200px;height:626px;
  background:radial-gradient(ellipse at 60% 55%,#3d4258 0%,var(--navy-dark) 70%)}
.reviews h2{left:0;width:1200px;text-align:center;top:76px;color:var(--white);font-size:24px;font-weight:700}
.quote{left:298px;width:630px;color:#e6e8ef;font-style:italic;font-size:16px;line-height:26px}
.qmark{left:244px;color:#5a5f75;font-family:Georgia,serif;font-size:90px;line-height:1}
.author{left:770px;color:var(--white)}
.author b{display:block;font-family:'Montserrat',sans-serif;font-size:16px;font-weight:700}
.author small{font-size:11.5px;color:#c0c4d0}

/* objects */
.objects-title{left:125px;top:2630px;color:var(--blue);font-size:25px;font-weight:700}
.objects-lead{left:125px;top:2676px;width:640px;font-size:12px;line-height:18px;color:#333}
.obj{top:2744px;width:462px;height:337px}
.obj .frame{position:absolute;left:22px;top:22px;right:22px;bottom:22px;border:2px solid var(--white)}
.obj h3{position:absolute;left:40px;top:196px;color:var(--white);font-size:17px;font-weight:700}
.obj p{position:absolute;left:40px;top:220px;color:#eef;font-size:12px}
.obj .btn{position:absolute;left:40px;top:252px;width:167px;height:37px;font-size:12px}

/* contact */
.contact{position:absolute;left:0;top:3180px;width:1200px;height:605px;background:#ededed}
.brand-foot{left:289px;top:112px;color:var(--navy);font-size:22px}
.brand-foot .mark{background:var(--navy);width:18px;height:18px}
.info{left:289px;display:flex;align-items:center;gap:18px;font-size:14.5px;line-height:23px;color:#222}
.info svg{flex:none}
.contact h2{left:613px;top:78px;color:var(--blue);font-size:25px;font-weight:700}
.lbl{left:613px;font-family:'Montserrat',sans-serif;font-weight:700;font-size:10.5px;color:#222}
.field{left:613px;width:299px;height:33px;background:var(--white);border:1px solid #cfcfcf;font-size:11px;color:#aaa;padding:9px 9px}
.send{left:613px;top:461px;width:299px;height:39px;background:var(--blue);color:var(--white)}
.legal{left:741px;top:537px;font-size:13px;color:#222}
.legal a{color:#222}
</style>
</head>
<body>

<header class="hero" role="img" aria-label="Foto: Altstadt mit Burg und Dächern in der Abenddämmerung, dunkelblau überlagert">
  <div class="abs brand brand-hero"><span class="mark"></span>WOHNWERK FRANKEN</div>
  <nav class="abs nav"><span>Mieter/Käufer</span><span>Vermieter/Verkäufer</span><span>Bauträger</span><span>Service</span><span>Über uns</span></nav>
  <h1 class="abs">Ihr Immobilienmakler für<br>die Metropolregion Nürnberg</h1>
  <div class="abs tile" style="left:126px">
    <svg width="60" height="58" viewBox="0 0 60 58" fill="none" stroke="#fff" stroke-width="1.6"><circle cx="16" cy="12" r="7"/><path d="M4 50V30c0-6 5-9 12-9s12 3 12 9v20"/><circle cx="42" cy="14" r="7"/><path d="M30 50V32c0-6 5-9 12-9s12 3 12 9v18"/><circle cx="29" cy="36" r="5"/><path d="M21 56v-8c0-4 4-6 8-6s8 2 8 6v8"/></svg>
    <span>Mieter/<br>Käufer</span>
  </div>
  <div class="abs tile" style="left:288px">
    <svg width="60" height="58" viewBox="0 0 60 58" fill="none" stroke="#fff" stroke-width="1.6"><path d="M4 28L30 6l26 22"/><path d="M10 24v28h40V24"/><rect x="16" y="32" width="10" height="8"/><rect x="34" y="32" width="10" height="20"/><rect x="38" y="8" width="6" height="10"/></svg>
    <span>Vermieter/<br>Verkäufer</span>
  </div>
  <div class="abs tile" style="left:449px">
    <svg width="60" height="58" viewBox="0 0 60 58" fill="none" stroke="#fff" stroke-width="1.6"><path d="M14 56V10h6v46"/><path d="M14 10h40v6H8"/><path d="M14 18l6 6M20 24l-6 6M14 30l6 6M20 36l-6 6M14 42l6 6"/><path d="M46 16v14"/><rect x="42" y="30" width="8" height="6"/><path d="M6 56h24"/></svg>
    <span>Bauträger</span>
  </div>
</header>

<section class="intro">
  <h2 class="abs">Die richtige Wahl des Immobilienmaklers</h2>
  <p class="abs" style="top:134px">Herzlich Willkommen bei der Lukas Brennholt Immobilienberatung in Nürnberg! Sie suchen den passenden Partner rund um das umfassende Thema Immobilien? Dann sind Sie hier genau richtig: egal ob Suche, Verkauf oder Vermietung einer Eigentumswohnung oder eines Hauses. Bei einem so komplexen Thema mit hohen Emotionen, Sachwerten und Auswirkungen auf Ihr tägliches Leben geht es um Vertrauen und ein gutes Gefühl. Sie sollen eine überzeugende Dienstleistung von Ihrem Makler erhalten.<br>Eine umfassende und professionelle Beratung ist dabei für Ihre Zufriedenheit entscheidend. Davon können Sie sich als Eigentümer schon beim ersten gemeinsamen Schritt überzeugen: der transparenten Einwertung Ihrer Immobilie.</p>
  <p class="abs" style="top:274px">Vertrauen Sie bei der Wahl des Maklers auf die Kombination aus Ausbildung, Erfahrung und Engagement. Als ausgebildeter Immobilienkaufmann (IHK) war bzw. bin ich als selbstständiger Kooperationspartner für namhafte Bauträger wie die Hallerbau AG, die Rothmann Gruppe GmbH oder die Kessler Bau GmbH &amp; Co. KG tätig. Daraus resultiert eine sehr gute Kenntnis des regionalen Immobilienmarktes in Nürnberg, Fürth, Erlangen, Schwabach und der weiteren Umgebung. Sie werden den Unterschied merken!</p>
  <div class="abs cta-q">Sie sind Eigentümer einer Immobilie?</div>
  <div class="abs btn">→ Jetzt bewerten lassen</div>
</section>

<div class="abs kicker">Das können wir für Sie tun</div>
<h2 class="abs services-title">Wenn Sie eine Immobilie verkaufen oder vermieten möchten</h2>
<div class="abs all-link">→ Alle Leistungen</div>

<div class="abs grid">
  <div class="ph" style="left:0;top:0;width:475px;height:237.5px;background:linear-gradient(180deg,#8a9cc8 0%,#c7b7d6 45%,#3e4a6e 100%)" role="img" aria-label="Foto: Einfamilienhaus mit dunklem Giebeldach"></div>
  <div class="cell cell-blue" style="left:475px;top:0">
    <h3>VERMARKTUNG</h3>
    <p>Gemeinsam legen wir ein Konzept fest, wie Ihre Immobilie am besten präsentiert wird. Dazu erhalten Sie einen ausführlichen Vorschlag mit vielen Auswahlmöglichkeiten, den wir an Ihre Wünsche und Vorstellungen anpassen.</p>
  </div>
  <div class="ph" style="left:712.5px;top:0;width:237.5px;height:237.5px;background:linear-gradient(135deg,#b08a5e 0%,#d9b995 50%,#6a4b35 100%)" role="img" aria-label="Foto: Frau mit Smartphone am Laptop"></div>
  <div class="notch" style="left:712px;top:107px;border-left:12px solid var(--blue)"></div>

  <div class="cell cell-text" style="left:0;top:237.5px">
    <h3>OBJEKTAUFNAHME</h3>
    <p>Die ersten Schritte sind die detaillierte Einwertung, Preisfindung, Vermessung und Fotografie Ihrer Immobilie. Daraus entsteht das Exposé u.a. mit hochwertigen Bildern und einer ausführlichen Beschreibung.</p>
  </div>
  <div class="ph" style="left:237.5px;top:237.5px;width:237.5px;height:237.5px;background:linear-gradient(180deg,#3d4a66 0%,#8a8f98 55%,#4a4c50 100%)" role="img" aria-label="Foto: Hauseingang mit blauer Tür und Garage"></div>
  <div class="notch" style="left:237px;top:345px;border-left:12px solid #fff"></div>
  <div class="ph" style="left:475px;top:237.5px;width:237.5px;height:237.5px;background:linear-gradient(90deg,#a9c97a 0%,#dfeac8 45%,#7a5a3a 85%,#4e3a28 100%)" role="img" aria-label="Foto: Schlüssel steckt im Türschloss"></div>
  <div class="notch" style="left:701px;top:345px;border-right:12px solid #fff"></div>
  <div class="cell cell-text right" style="left:712.5px;top:237.5px">
    <h3>VERTRAGSABSCHLUSS</h3>
    <p>Danach folgt die Vorbereitung und Unterzeichnung des Vertrages. Dabei werden die Interessen aller Parteien berücksichtigt und ausführlich besprochen. Alle Parteien sollen mit dem Abschluss vollkommen zufrieden sein.</p>
  </div>
</div>

<section class="reviews" role="img" aria-label="Foto: Familie mit Kind, stark abgedunkelt im Hintergrund">
  <h2 class="abs">Das sagen unsere Kunden über uns</h2>
  <div class="abs qmark" style="top:160px">”</div>
  <p class="abs quote" style="top:160px">Äußerst kundenorientiertes und freundliches Auftreten. Sehr große Fachkompetenz sowie überaus seriöse Abwicklung bei Kauf bzw. Verkauf als auch bei Vermietung von Objekten. Kann man wirklich zu 100% weiterempfehlen!</p>
  <div class="abs author" style="top:246px"><b>Sabine und Jörg M.</b><small>(Käufer und Vermieter)</small></div>
  <div class="abs qmark" style="top:384px">”</div>
  <p class="abs quote" style="top:384px">Ich würde Herrn Brennholt als freundlich, zuverlässig und integer beschreiben. Eigenschaften, die in dieser Kombination nicht branchentypisch sind. Er hat uns beim Erwerb einer Eigentumswohnung sehr kompetent beraten und bis zum Abschluss herausragend begleitet. Ich kann die "Lukas Brennholt Immobilienberatung" wirklich uneingeschränkt empfehlen.</p>
  <div class="abs author" style="top:522px"><b>Henrik W.</b><small>(Käufer)</small></div>
</section>

<h2 class="abs objects-title">Erfolgreich vermittelte Objekte</h2>
<p class="abs objects-lead">Lorem ipsum dolor sit amet, consetetur sadipscing elitr, sed diam nonumy eirmod tempor invidunt ut labore et dolore magna aliquyam erat, sed diam voluptua.</p>

<div class="abs obj" style="left:125px;background:linear-gradient(180deg,#8fa6cf 0%,#b9c4d6 45%,#5d6270 80%,#3a3d44 100%)" role="img" aria-label="Foto: moderner Mehrfamilien-Neubau mit Balkonen">
  <div class="frame"></div>
  <h3>Exklusiv und ruhig</h3>
  <p>Lorem ipsum dolor sit amet</p>
  <div class="btn">→ Objekt ansehen</div>
</div>
<div class="abs obj" style="left:613px;background:linear-gradient(180deg,#9db4d8 0%,#c9ced6 40%,#6a6e76 80%,#3c3f45 100%)" role="img" aria-label="Foto: weißes Einfamilienhaus mit Satteldach">
  <div class="frame"></div>
  <h3>Moderner Luxus</h3>
  <p>Lorem ipsum dolor sit amet</p>
  <div class="btn">→ Objekt ansehen</div>
</div>

<section class="contact">
  <div class="abs brand brand-foot"><span class="mark"></span>WOHNWERK FRANKEN</div>

  <div class="abs info" style="top:222px">
    <svg width="42" height="36" viewBox="0 0 42 36" fill="var(--navy)"><path d="M21 2L1 19h6v15h10v-9h8v9h10V19h6z"/></svg>
    <span>Lindenhofweg 12<br>90480 Nürnberg</span>
  </div>
  <div class="abs info" style="top:300px">
    <svg width="42" height="36" viewBox="0 0 42 36" fill="var(--navy)"><path d="M4 10c0-5 8-7 17-7s17 2 17 7v4h-9v-4H13v4H4z"/><path d="M10 16h22l4 18H6z"/><circle cx="21" cy="25" r="5" fill="#ededed"/></svg>
    <span>0911 5550 2040</span>
  </div>
  <div class="abs info" style="top:363px">
    <svg width="42" height="36" viewBox="0 0 42 36"><rect x="13" y="1" width="16" height="34" rx="3" fill="var(--navy)"/><rect x="16" y="5" width="10" height="24" fill="#ededed"/></svg>
    <span>0176 5550 1188</span>
  </div>
  <div class="abs info" style="top:426px">
    <svg width="42" height="36" viewBox="0 0 42 36" fill="var(--navy)"><path d="M40 2L2 17l12 4 2 13 6-9 10 7z"/></svg>
    <span>lb@wohnwerkfranken.de</span>
  </div>

  <h2 class="abs">Wir sind gerne für Sie da:</h2>
  <div class="abs lbl" style="top:141px">Vollständiger Name</div>
  <div class="abs field" style="top:157px">z.B. Max Mustermann</div>
  <div class="abs lbl" style="top:210px">E-Mail</div>
  <div class="abs field" style="top:226px">z.B. mustermann@email.de</div>
  <div class="abs lbl" style="top:279px">Telefon</div>
  <div class="abs field" style="top:295px">Wie erreichen wir Sie am besten?</div>
  <div class="abs lbl" style="top:348px">Was möchten Sie uns mitteilen?</div>
  <div class="abs field" style="top:365px;height:80px">Ihre Nachricht</div>
  <div class="abs btn send">→ Nachricht absenden</div>
  <div class="abs legal"><a href="#">Datenschutz</a> | <a href="#">Impressum</a></div>
</section>

</body>
</html>
```